Business Card - connecting 2 souls and beggining the journey of self discovery

Logo on the front
with tag line

On the back list of services and contact details

Seminars
workshops
Coaching
podcasts

Daniel Porthwick
Health & Wellbeing Life Coach
0491 372 815
daniel@wovenpathwellness.example
wovenpathwellness.example

Industry/Entity Type

Life Coaching

Contact Information for Business Card

I like the use of colour from the logo to be used. I'm not a fan of white.

Requirements
Must have
• My tagline: The journey home starts with you
Nice to have
• Use of colour that is in the mind body soul logo

```html
<!DOCTYPE html>
<html lang="en">
<head>
<meta charset="utf-8">
<title>Woven Path Wellness – Business Card</title>
<link rel="stylesheet" href="https://fonts.googleapis.com/css2?family=Open+Sans:wght@400;600;700&display=swap">
<style>
  :root {
    --stage: #e9e7e4;
    --card-white: #f8f8f7;
    --band-grey: #8d8d8f;
    --band-grey-light: #a4a4a6;
    --ink: #4a4a4c;
    --ink-soft: #5b5b5e;
    --orange: #f2913f;
    --coral: #ec6a5e;
    --red: #e0574f;
    --green: #6cbf5f;
    --teal: #2fa58e;
    --purple: #8c4db4;
    --white: #ffffff;
  }
  * { box-sizing: border-box; margin: 0; padding: 0; }
  html, body { width: 1200px; height: 960px; overflow: hidden; }
  body {
    background: var(--stage);
    font-family: "Open Sans", Arial, sans-serif;
    position: relative;
  }
  .card {
    position: absolute;
    left: 250px;
    width: 700px;
    height: 400px;
    overflow: hidden;
    box-shadow: 0 6px 18px rgba(0,0,0,0.18);
  }

  /* Front */
  .card-front {
    top: 45px;
    background: radial-gradient(ellipse at 50% 45%, #f5a23c 0%, var(--orange) 30%, var(--coral) 75%, var(--red) 100%);
    display: flex;
    flex-direction: column;
    align-items: center;
    justify-content: center;
    gap: 18px;
  }
  .front-mark {
    width: 96px;
    height: 96px;
    border-radius: 50%;
    background: rgba(255,255,255,0.28);
  }
  .front-name {
    font-size: 34px;
    font-weight: 600;
    color: var(--white);
    letter-spacing: -0.5px;
  }

  /* Back */
  .card-back {
    top: 495px;
    background: var(--card-white);
  }
  .back-shape { position: absolute; inset: 0; }
  .brand {
    position: absolute;
    left: 48px;
    top: 34px;
  }
  .brand-mark {
    width: 66px;
    height: 66px;
    border-radius: 50%;
    background: var(--orange);
    margin-left: 120px;
    margin-bottom: 12px;
  }
  .brand-name {
    font-size: 29px;
    font-weight: 400;
    color: var(--ink-soft);
    letter-spacing: -0.5px;
    line-height: 1.1;
  }
  .tagline {
    font-size: 17px;
    font-weight: 600;
    color: var(--ink);
    margin-top: 2px;
  }
  .contact {
    position: absolute;
    left: 48px;
    top: 212px;
    list-style: none;
    font-size: 18px;
    color: var(--ink);
    line-height: 1.28;
  }
  .contact li { display: flex; align-items: center; gap: 9px; }
  .contact svg { width: 14px; height: 14px; fill: var(--teal); flex: none; }
  .services {
    position: absolute;
    left: 40px;
    top: 318px;
    font-size: 17px;
    color: var(--ink);
  }
  .services .dot { color: var(--teal); font-weight: 700; margin: 0 3px; }
  .person {
    position: absolute;
    right: 18px;
    top: 0;
    height: 400px;
    display: flex;
    flex-direction: row;
    justify-content: center;
    align-items: center;
    gap: 4px;
    writing-mode: vertical-rl;
    transform: rotate(180deg);
    color: var(--white);
    text-transform: uppercase;
  }
  .person-name { font-size: 25px; font-weight: 700; letter-spacing: 0.3px; }
  .person-role { font-size: 18px; font-weight: 400; letter-spacing: 0.3px; }
</style>
</head>
<body>

  <section class="card card-front" aria-label="Card front">
    <div class="front-mark"></div>
    <div class="front-name">Woven Path Wellness</div>
  </section>

  <section class="card card-back" aria-label="Card back">
    <svg class="back-shape" viewBox="0 0 700 400" width="700" height="400" aria-hidden="true">
      <defs>
        <linearGradient id="band-fill" x1="0" y1="0" x2="1" y2="0">
          <stop offset="0" stop-color="var(--band-grey-light)"/>
          <stop offset="1" stop-color="var(--band-grey)"/>
        </linearGradient>
        <linearGradient id="arc-colours" gradientUnits="userSpaceOnUse" x1="0" y1="0" x2="0" y2="400">
          <stop offset="0" stop-color="#f2913f"/>
          <stop offset="0.2" stop-color="#e0574f"/>
          <stop offset="0.2" stop-color="#ffffff"/>
          <stop offset="0.235" stop-color="#ffffff"/>
          <stop offset="0.235" stop-color="#6cbf5f"/>
          <stop offset="0.62" stop-color="#6cbf5f"/>
          <stop offset="0.62" stop-color="#ffffff"/>
          <stop offset="0.655" stop-color="#ffffff"/>
          <stop offset="0.655" stop-color="#8c4db4"/>
          <stop offset="0.84" stop-color="#8c4db4"/>
          <stop offset="1" stop-color="#8c4db4" stop-opacity="0"/>
        </linearGradient>
      </defs>
      <path class="grey-band" d="M540,0 Q680,190 420,400 L700,400 L700,0 Z" fill="url(#band-fill)"/>
      <path class="colour-arc" d="M540,0 Q680,190 420,400" fill="none" stroke="url(#arc-colours)" stroke-width="9"/>
      <path class="arc-inner-line" d="M532,0 Q670,190 410,400" fill="none" stroke="#ffffff" stroke-width="3"/>
    </svg>

    <div class="brand">
      <div class="brand-mark"></div>
      <div class="brand-name">Woven Path Wellness</div>
      <div class="tagline">The journey home starts with you</div>
    </div>

    <ul class="contact">
      <li>
        <svg viewBox="0 0 16 16"><path d="M3.6 1.5l2.3 2.6-1.3 1.9c.9 2 2.5 3.6 4.5 4.5l1.9-1.3 2.6 2.3-1.4 2.3C6.7 14.2 1.8 9.3 1.3 3z"/></svg>
        0491 372 815
      </li>
      <li>
        <svg viewBox="0 0 16 16"><path d="M1 3h14v10H1z M1 3l7 5.5L15 3" stroke="#f8f8f7" stroke-width="1.2"/></svg>
        daniel@wovenpathwellness.example
      </li>
      <li>
        <svg viewBox="0 0 16 16"><circle cx="8" cy="8" r="7"/></svg>
        www.wovenpathwellness.example
      </li>
    </ul>

    <p class="services">Seminars <span class="dot">•</span> Workshops <span class="dot">•</span> Coaching <span class="dot">•</span> Podcasts</p>

    <div class="person">
      <span class="person-name">Daniel Porthwick</span>
      <span class="person-role">Health &amp; Wellbeing Life Coach</span>
    </div>
  </section>

</body>
</html>
```